Can you create a Business Card based on the Logo you designed.

See example and would like to see other examples.

Trying to keep it very clean with a focus on the logo and name.

```html
<!DOCTYPE html>
<html lang="en">
<head>
<meta charset="UTF-8">
<title>Verdano Business Card</title>
<link rel="stylesheet" href="https://fonts.googleapis.com/css2?family=Ubuntu:wght@400;500;700&display=swap">
<style>
  :root {
    --backdrop: #979797;
    --brand-green: #0b7343;
    --leaf-green: #7dc242;
    --sun-orange: #f39c33;
    --card-white: #ffffff;
    --text-grey: #8a8a8a;
  }
  * { box-sizing: border-box; margin: 0; padding: 0; }
  html, body {
    width: 1200px;
    height: 1200px;
    overflow: hidden;
    background: var(--backdrop);
    font-family: "Ubuntu", sans-serif;
  }
  .card {
    position: absolute;
    top: 228px;
    width: 436px;
    height: 745px;
    border-radius: 20px;
    overflow: hidden;
  }
  .card--front {
    left: 162px;
    background: var(--brand-green);
    display: flex;
    align-items: center;
    justify-content: center;
  }
  .card--back {
    left: 660px;
    background: var(--card-white);
    text-align: center;
  }
  .wordmark {
    font-weight: 500;
    letter-spacing: 1px;
    line-height: 1;
  }
  .card--front .wordmark {
    color: var(--card-white);
    font-size: 84px;
    margin-top: -20px;
  }
  .card--back .wordmark {
    color: var(--brand-green);
    font-size: 48px;
    position: absolute;
    top: 148px;
    left: 0;
    right: 0;
  }
  .holder-name {
    position: absolute;
    top: 266px;
    left: 0;
    right: 0;
    color: var(--leaf-green);
    font-size: 40px;
    font-weight: 500;
  }
  .holder-title {
    position: absolute;
    top: 318px;
    left: 0;
    right: 0;
    color: var(--sun-orange);
    font-size: 14px;
    letter-spacing: 1.6px;
    text-transform: uppercase;
  }
  .contact-icons {
    position: absolute;
    top: 355px;
    left: 0;
    right: 0;
    display: flex;
    justify-content: center;
    gap: 6px;
  }
  .contact-icons svg { width: 34px; height: 34px; }
  .contact-lines {
    position: absolute;
    top: 402px;
    left: 0;
    right: 0;
    list-style: none;
    color: var(--text-grey);
    font-size: 20px;
    line-height: 27px;
  }
  .corner-decoration {
    position: absolute;
    right: 0;
    bottom: 0;
    width: 271px;
    height: 242px;
    border-top-left-radius: 160px;
    background: linear-gradient(160deg, var(--sun-orange) 0%, var(--sun-orange) 30%, var(--leaf-green) 60%);
  }
</style>
</head>
<body>
  <section class="card card--front">
    <div class="wordmark">Verdano</div>
  </section>

  <section class="card card--back">
    <div class="wordmark">Verdano</div>
    <h1 class="holder-name">Marcus Hale</h1>
    <p class="holder-title">Chief Executive Officer</p>

    <div class="contact-icons">
      <svg viewBox="0 0 34 34" aria-label="Phone">
        <circle cx="17" cy="17" r="16" fill="var(--brand-green)"/>
        <rect x="12" y="8" width="10" height="18" rx="2" fill="none" stroke="#fff" stroke-width="1.6"/>
        <circle cx="17" cy="23" r="1" fill="#fff"/>
      </svg>
      <svg viewBox="0 0 34 34" aria-label="Email">
        <circle cx="17" cy="17" r="16" fill="var(--brand-green)"/>
        <rect x="9" y="11" width="16" height="12" rx="1" fill="none" stroke="#fff" stroke-width="1.6"/>
        <polyline points="9,11 17,18 25,11" fill="none" stroke="#fff" stroke-width="1.6"/>
      </svg>
      <svg viewBox="0 0 34 34" aria-label="Website">
        <circle cx="17" cy="17" r="16" fill="var(--brand-green)"/>
        <circle cx="17" cy="17" r="8" fill="none" stroke="#fff" stroke-width="1.5"/>
        <ellipse cx="17" cy="17" rx="3.5" ry="8" fill="none" stroke="#fff" stroke-width="1.3"/>
        <line x1="9" y1="17" x2="25" y2="17" stroke="#fff" stroke-width="1.3"/>
        <line x1="10.5" y1="13" x2="23.5" y2="13" stroke="#fff" stroke-width="1.1"/>
        <line x1="10.5" y1="21" x2="23.5" y2="21" stroke="#fff" stroke-width="1.1"/>
      </svg>
    </div>

    <ul class="contact-lines">
      <li>+1 (555) 014-2271</li>
      <li>ceo@verdanofarm.com</li>
      <li>www.verdanofarm.com</li>
    </ul>

    <div class="corner-decoration" role="img" aria-label="Large brand emblem decoration of leaves and rising sun"></div>
  </section>
</body>
</html>
```